Florida-based Coastal Landscaping Comapny Needs Postcard Designs

We are a newly established Florida-based, coastal landscaping company that is looking for some really innovative postcards that we can use to get our name our to affluent consumers that live on the coast of Florida (think on the beach) and small to medium sized businesses in the same area. We will be sending out 100s of thousands of these, so need a great design

Target Market(s)

Affluent consumers and small to medium sized businesses

Industry/Entity Type

Landscaping

Font styles to use
Sans Serif

Colors

Designer to choose colors to be used in the design.

Requirements
Must have
• Florida - looking, island looking / paradise, but incorporate landscaping themes
• Need to say something about "Enjoy your yard this summer" or something relating to summer, landscapes and florida
• and would like to make two offers $50.00 off with signing up for one of our routine maintenance programs, or 1 free landscape inspection
Should not have
• Regular generic lawn company designs. We are a top tier landscape design / build plus maintenance firm, so not your mom and pop lawn mowing company

```html
<!DOCTYPE html>
<html lang="en">
<head>
<meta charset="utf-8">
<title>ShoreScape Summer Postcard</title>
<link rel="stylesheet" href="https://fonts.googleapis.com/css2?family=Lato:ital,wght@0,400;0,700;1,400;1,700&family=Roboto+Condensed:wght@400;700&family=Libre+Baskerville&display=swap">
<style>
  :root {
    --cyan: #1ba6d4;
    --navy: #1d3550;
    --ink: #1e1e1e;
    --white: #ffffff;
    --sky: #3f8fd2;
    --sky-light: #a9d0ee;
    --house: #bfe3dc;
    --palm: #4f8a2e;
    --palm-sun: #d9d23a;
    --gravel: #f2efe6;
    --lawn: #5f9440;
    --stage: #ececec;
    --line: #8a8a8a;
  }
  * { margin: 0; padding: 0; box-sizing: border-box; }
  html, body { width: 1200px; height: 1200px; overflow: hidden; background: var(--stage); }
  .canvas { position: relative; width: 1200px; height: 1200px; }

  .card {
    position: absolute; left: 252px; width: 812px; height: 629px;
    transform: scale(0.857); transform-origin: top left;
    overflow: hidden; background: var(--white);
    box-shadow: 0 6px 18px rgba(0,0,0,0.18);
    font-family: "Lato", sans-serif;
  }
  .card--front { top: 30px; }
  .card--back { top: 609px; }

  .abs { position: absolute; }
  .cond { font-family: "Roboto Condensed", sans-serif; }

  /* front */
  .hero-photo {
    position: absolute; inset: 0;
    background:
      linear-gradient(180deg, rgba(255,255,255,0.96) 0%, rgba(255,255,255,0.7) 14%, rgba(255,255,255,0) 30%),
      radial-gradient(ellipse 140px 190px at 450px 250px, rgba(224,214,58,0.9), rgba(224,214,58,0) 75%),
      radial-gradient(ellipse 170px 200px at 770px 330px, rgba(79,138,46,0.95), rgba(79,138,46,0) 75%),
      radial-gradient(ellipse 130px 180px at 70px 330px, rgba(60,120,50,0.9), rgba(60,120,50,0) 75%),
      radial-gradient(ellipse 300px 90px at 340px 470px, rgba(242,239,230,1), rgba(242,239,230,0) 80%),
      radial-gradient(ellipse 360px 120px at 400px 360px, rgba(191,227,220,1), rgba(191,227,220,0.6) 60%, rgba(191,227,220,0) 100%),
      radial-gradient(ellipse 220px 70px at 200px 230px, rgba(255,255,255,0.85), rgba(255,255,255,0) 80%),
      radial-gradient(ellipse 260px 80px at 620px 200px, rgba(255,255,255,0.7), rgba(255,255,255,0) 80%),
      linear-gradient(180deg, var(--sky-light) 0%, var(--sky) 40%, #6fb0df 58%, var(--house) 66%, var(--lawn) 80%, #7fae55 100%);
  }
  .front-shapes { position: absolute; inset: 0; }

  .brand { left: 34px; top: 38px; font-size: 29px; font-weight: 400; letter-spacing: 1px; color: var(--navy); }
  .brand-dot { display: inline-block; width: 12px; height: 12px; border-radius: 50%; background: var(--cyan); margin-right: 8px; vertical-align: middle; }
  .tagline { left: 30px; top: 80px; font-size: 26px; color: var(--cyan); letter-spacing: -0.4px; }
  .tagline-sub { left: 30px; top: 114px; font-size: 20px; color: var(--ink); font-family: "Libre Baskerville", serif; letter-spacing: -0.6px; }

  .pitch { right: 21px; top: 16px; text-align: right; font-size: 22px; line-height: 26.5px; color: var(--ink); }
  .pitch strong { color: var(--cyan); font-weight: 700; }

  .offer-lead { right: 21px; top: 377px; font-size: 22px; font-weight: 700; color: var(--ink); letter-spacing: 0.3px; }
  .offer-main { right: 21px; top: 412px; font-size: 40px; font-weight: 700; color: var(--cyan); }
  .offer-note { left: 553px; top: 460px; width: 252px; text-align: center; font-size: 16px; line-height: 21px; color: var(--white); white-space: nowrap; }
  .offer-alt { right: 21px; top: 525px; font-size: 21px; color: var(--ink); }
  .offer-alt b { color: var(--cyan); }
  .offer-phone { right: 21px; top: 553px; font-size: 22px; font-weight: 700; color: var(--ink); display: flex; align-items: center; gap: 6px; }

  .services-title { left: 19px; top: 497px; font-size: 19px; font-weight: 700; color: var(--white); }
  .services { left: 19px; top: 522px; color: var(--white); font-size: 16px; line-height: 21.5px; }
  .services li { list-style: none; display: flex; align-items: center; gap: 5px; }
  .services .pair { gap: 16px; }
  .services span { display: inline-flex; align-items: center; gap: 5px; }
  .contact-row { display: flex; align-items: center; gap: 6px; color: var(--white); font-size: 16px; }
  .front-contact { left: 19px; top: 592px; gap: 16px; }
  .front-contact span { display: inline-flex; align-items: center; gap: 6px; }

  /* back */
  .letter-panel { position: absolute; left: 0; top: 0; width: 516px; height: 629px;
    background: linear-gradient(180deg, #dcf0fb 0%, #ffffff 40%, #ffffff 100%); }
  .letter { left: 28px; top: 22px; width: 474px; font-style: italic; font-size: 13.3px; line-height: 17px; color: var(--ink); text-align: justify; }
  .letter p + p { margin-top: 6px; }
  .signoff { left: 380px; top: 292px; text-align: right; font-style: italic; font-weight: 700; font-size: 13.5px; line-height: 17px; color: var(--ink); width: 108px; }
  .estate-photo { position: absolute; left: 0; top: 285px; width: 516px; height: 255px;
    background:
      radial-gradient(ellipse 110px 130px at 40px 140px, rgba(110,140,90,0.95), rgba(110,140,90,0) 80%),
      radial-gradient(ellipse 150px 80px at 180px 110px, rgba(236,226,190,1), rgba(236,226,190,0) 85%),
      radial-gradient(ellipse 150px 80px at 400px 120px, rgba(130,160,100,0.9), rgba(130,160,100,0) 80%),
      radial-gradient(ellipse 140px 40px at 240px 200px, rgba(220,214,200,1), rgba(220,214,200,0) 85%),
      linear-gradient(180deg, #ffffff 0%, #dbe9f3 16%, #c9d8c0 40%, #8fb06a 68%, #77a84c 100%); }
  .garden-circle { position: absolute; border-radius: 50%; border: 4px solid var(--white); box-shadow: 0 3px 8px rgba(0,0,0,0.25); }
  .garden-circle--one { left: 270px; top: 438px; width: 124px; height: 124px; background: radial-gradient(circle at 50% 55%, #d98a6a 0%, #6fa24c 35%, #3e6e32 100%); }
  .garden-circle--two { left: 394px; top: 456px; width: 114px; height: 114px; background: linear-gradient(180deg, #c7e1f2 0%, #e3c59c 45%, #6f9d4c 70%, #86b15b 100%); }
  .back-contact { left: 20px; top: 561px; display: flex; flex-direction: column; gap: 8px; }
  .back-contact .row { display: flex; align-items: center; gap: 16px; }
  .back-contact span { display: inline-flex; align-items: center; gap: 6px; color: var(--white); font-size: 16px; }
  .stamp-box { left: 683px; top: 30px; width: 98px; height: 122px; background: #eeeeee; border: 1px solid #9a9a9a; }
  .address-line { position: absolute; left: 540px; width: 242px; height: 0; border-top: 1px solid var(--line); }
</style>
</head>
<body>
<div class="canvas">

  <section class="card card--front">
    <div class="hero-photo" role="img" aria-label="Photo of a pale blue Florida beach house with white porch, palm trees and tropical planting under a bright blue sky"></div>
    <svg class="front-shapes" viewBox="0 0 812 629" width="812" height="629">
      <path d="M0,472 C140,455 290,470 380,525 L812,525 L812,629 L0,629 Z" fill="var(--cyan)"/>
      <path d="M0,472 C140,455 290,470 380,525" fill="none" stroke="#ffffff" stroke-width="4"/>
      <path d="M365,522 C460,460 570,360 812,338 L812,596 C640,616 470,590 365,522 Z" fill="#ffffff"/>
      <path d="M600,370 C680,352 750,345 812,344" fill="none" stroke="#8d8d8d" stroke-width="9" opacity="0.85"/>
      <path d="M365,522 C460,460 570,360 812,338" fill="none" stroke="var(--cyan)" stroke-width="5"/>
      <path d="M365,522 C470,590 640,616 812,596" fill="none" stroke="var(--cyan)" stroke-width="4"/>
      <path d="M595,408 L812,408 L812,452 L580,452 Z" fill="#f4f4f4" stroke="#cfcfcf"/>
      <rect x="553" y="456" width="252" height="48" rx="20" fill="var(--cyan)"/>
    </svg>

    <div class="abs brand"><span class="brand-dot"></span>SHORESCAPE</div>
    <div class="abs tagline">The grass is always greener</div>
    <div class="abs tagline-sub">ON YOUR SIDE OF THE FENCE</div>

    <div class="abs pitch cond">
      <strong>Your family deserves the best</strong><br>
      outdoor experience this summer.<br>
      <strong>Why not create it at your</strong><br>
      HOME'S BACK YARD?
    </div>

    <div class="abs offer-lead cond">CALL US NOW AND</div>
    <div class="abs offer-main cond">Get $50 off</div>
    <div class="abs offer-note cond">when signing up for one of our<br>routine maintenance programs</div>
    <div class="abs offer-alt cond">or <b>1 FREE</b> landscape/irrigation inspection</div>
    <div class="abs offer-phone cond">
      <svg width="20" height="20" viewBox="0 0 20 20"><circle cx="10" cy="10" r="9" fill="none" stroke="var(--cyan)" stroke-width="1.5"/><path d="M7,5 L9,7.5 L8,9 C8.7,10.6 9.6,11.5 11,12 L12.5,11 L15,13 L13.5,15 C9,14.5 5.5,11 5,6.5 Z" fill="var(--cyan)"/></svg>
      (555) 014-2277
    </div>

    <div class="abs services-title cond">Our Services</div>
    <ul class="abs services">
      <li class="pair">
        <span><svg width="15" height="15" viewBox="0 0 15 15"><circle cx="7.5" cy="7.5" r="6.5" fill="none" stroke="#fff" stroke-width="1.4"/><path d="M4.3,7.7 L6.6,10 L10.8,5.2" fill="none" stroke="#fff" stroke-width="1.5"/></svg>Landscaping</span>
        <span><svg width="15" height="15" viewBox="0 0 15 15"><circle cx="7.5" cy="7.5" r="6.5" fill="none" stroke="#fff" stroke-width="1.4"/><path d="M4.3,7.7 L6.6,10 L10.8,5.2" fill="none" stroke="#fff" stroke-width="1.5"/></svg>Landscape maintenance</span>
      </li>
      <li><svg width="15" height="15" viewBox="0 0 15 15"><circle cx="7.5" cy="7.5" r="6.5" fill="none" stroke="#fff" stroke-width="1.4"/><path d="M4.3,7.7 L6.6,10 L10.8,5.2" fill="none" stroke="#fff" stroke-width="1.5"/></svg>Irrigation installation and maintenance</li>
      <li><svg width="15" height="15" viewBox="0 0 15 15"><circle cx="7.5" cy="7.5" r="6.5" fill="none" stroke="#fff" stroke-width="1.4"/><path d="M4.3,7.7 L6.6,10 L10.8,5.2" fill="none" stroke="#fff" stroke-width="1.5"/></svg>Sod installation Pressure washing</li>
    </ul>
    <div class="abs contact-row front-contact">
      <span><svg width="15" height="11" viewBox="0 0 15 11"><rect x="0.7" y="0.7" width="13.6" height="9.6" fill="none" stroke="#fff" stroke-width="1.2"/><path d="M0.7,0.7 L7.5,6 L14.3,0.7" fill="none" stroke="#fff" stroke-width="1.2"/></svg>hello@shorescapefl.com</span>
      <span><svg width="15" height="15" viewBox="0 0 15 15"><circle cx="7.5" cy="7.5" r="6.5" fill="none" stroke="#fff" stroke-width="1.2"/><ellipse cx="7.5" cy="7.5" rx="3" ry="6.5" fill="none" stroke="#fff" stroke-width="1.1"/><path d="M1,7.5 H14" stroke="#fff" stroke-width="1.1"/></svg>www.shorescapefl.com</span>
    </div>
  </section>

  <section class="card card--back">
    <div class="letter-panel"></div>
    <div class="estate-photo" role="img" aria-label="Photo of a two-storey coastal home with palms, lawn and a paved driveway"></div>
    <div class="abs letter">
      <p>Hi,<br>I'm sure you're busy so I'll be brief. As you know, summertime is ahead, a time to relax, unwind and spend quality time with your family. And what a better place to enjoy Florida's sunny weather than the privacy of your own home?</p>
      <p>It's just that your yard probably needs some attention before it can really be called your own piece of heaven. It may not seem like it right now, but your yard is just a small step away from becoming your family's outdoor sanctuary, or an amazing venue for a summer party with closest friends.</p>
      <p>This is where our talented experts step in. Our landscaping services are tailor-made to suit your every special need. We know how to adjust to your busy schedule and how to deliver results on time and within budget.</p>
      <p>Inform us of your landscaping needs, and use the special gift offer that we've prepared for you. Let the summer vacation come to your home this year. Thank you for your time.</p>
    </div>
    <div class="abs signoff">All the best,<br>ShoreScape</div>
    <svg class="abs" style="left:0;top:0" viewBox="0 0 516 629" width="516" height="629">
      <path d="M0,532 C140,515 330,520 516,560 L516,629 L0,629 Z" fill="var(--cyan)"/>
      <path d="M0,532 C140,515 330,520 516,560" fill="none" stroke="#ffffff" stroke-width="4"/>
    </svg>
    <div class="garden-circle garden-circle--one" role="img" aria-label="Photo of a lush tropical garden bed with colourful plants"></div>
    <div class="garden-circle garden-circle--two" role="img" aria-label="Photo of a Mediterranean-style estate with manicured lawn"></div>
    <div class="abs back-contact">
      <div class="row"><span><svg width="18" height="18" viewBox="0 0 20 20"><circle cx="10" cy="10" r="9" fill="none" stroke="#fff" stroke-width="1.5"/><path d="M7,5 L9,7.5 L8,9 C8.7,10.6 9.6,11.5 11,12 L12.5,11 L15,13 L13.5,15 C9,14.5 5.5,11 5,6.5 Z" fill="#fff"/></svg><b>(555) 014-2277</b></span></div>
      <div class="row">
        <span><svg width="17" height="17" viewBox="0 0 15 15"><circle cx="7.5" cy="7.5" r="6.5" fill="none" stroke="#fff" stroke-width="1.2"/><ellipse cx="7.5" cy="7.5" rx="3" ry="6.5" fill="none" stroke="#fff" stroke-width="1.1"/><path d="M1,7.5 H14" stroke="#fff" stroke-width="1.1"/></svg>www.shorescapefl.com</span>
        <span><svg width="20" height="14" viewBox="0 0 15 11"><rect x="0.7" y="0.7" width="13.6" height="9.6" fill="none" stroke="#fff" stroke-width="1.1"/><path d="M0.7,0.7 L7.5,6 L14.3,0.7" fill="none" stroke="#fff" stroke-width="1.1"/></svg>hello@shorescapefl.com</span>
      </div>
    </div>
    <div class="abs stamp-box"></div>
    <div class="address-line" style="top:346px"></div>
    <div class="address-line" style="top:394px"></div>
    <div class="address-line" style="top:443px"></div>
    <div class="address-line" style="top:490px"></div>
  </section>

</div>
</body>
</html>
```